Craft Beer Needs a Label/ Logo Design

Name: Tidewell
(Tidewell Ale, Tidewell Pilsner, Tidewell Stout)

We are looking for a logo-ed label that will resonate domestically and internationally for this new Craft Beer Brand.

Reason: Reviewing final and different versions submitted (edited)

Target Market(s)

Millenials

Logo Text

Tidewell Pilsner

Logo styles of interest
Emblem Logo
Character Logo
Colors

Designer to choose colors to be used in the design.

Requirements
Must have
• A labled logo design -- "Tidewell" is the name, but would like to see samples with "Ale", "Pilsner", or "Stout" after!

```html
<!DOCTYPE html>
<html lang="en">
<head>
<meta charset="utf-8">
<title>Tidewell Pilsner – Label</title>
<link rel="stylesheet" href="https://fonts.googleapis.com/css2?family=Alfa+Slab+One&family=Great+Vibes&family=Oswald:wght@600&display=swap">
<style>
  :root {
    --canvas-bg: #eeeeef;
    --label-blue: #2f6fa6;
    --label-blue-deep: #1d4d7c;
    --label-blue-light: #4d8cc2;
    --gold: #d9a93e;
    --gold-light: #f3d688;
    --ribbon-red: #c8203f;
    --ribbon-red-dark: #8e1329;
    --ribbon-red-light: #e03655;
    --ink-white: #ffffff;
    --ink-dark: #5a1020;
  }
  html, body {
    margin: 0;
    padding: 0;
    overflow: hidden;
  }
  body {
    width: 861px;
    height: 1200px;
    background: radial-gradient(circle at 50% 40%, #fafafa 0%, var(--canvas-bg) 70%);
    position: relative;
  }
  .beer-label {
    position: absolute;
    left: 160px;
    top: 190px;
    width: 540px;
    height: 800px;
    overflow: visible;
  }
  .label-script {
    font-family: "Great Vibes", cursive;
    fill: var(--ink-white);
  }
  .label-tagline {
    font-family: "Great Vibes", cursive;
    fill: var(--ribbon-red-dark);
  }
  .brand-name {
    font-family: "Alfa Slab One", serif;
    fill: var(--ink-white);
    letter-spacing: 2px;
  }
  .label-specs {
    font-family: "Oswald", sans-serif;
    font-weight: 600;
    fill: var(--ink-white);
  }
</style>
</head>
<body>
<svg class="beer-label" viewBox="0 0 540 800" xmlns="http://www.w3.org/2000/svg" aria-labelledby="label-title">
  <title id="label-title">Tidewell Pilsner craft beer label</title>
  <defs>
    <radialGradient id="label-field" cx="50%" cy="45%" r="60%">
      <stop offset="0%" stop-color="var(--label-blue-light)"/>
      <stop offset="60%" stop-color="var(--label-blue)"/>
      <stop offset="100%" stop-color="var(--label-blue-deep)"/>
    </radialGradient>
    <linearGradient id="gold-frame" x1="0" y1="0" x2="1" y2="1">
      <stop offset="0%" stop-color="var(--gold-light)"/>
      <stop offset="50%" stop-color="var(--gold)"/>
      <stop offset="100%" stop-color="var(--gold-light)"/>
    </linearGradient>
    <linearGradient id="ribbon-face" x1="0" y1="0" x2="0" y2="1">
      <stop offset="0%" stop-color="var(--ribbon-red-light)"/>
      <stop offset="100%" stop-color="var(--ribbon-red)"/>
    </linearGradient>
  </defs>

  <!-- label body -->
  <polygon class="label-frame-outer" points="270,0 540,130 540,670 270,800 0,670 0,130" fill="url(#gold-frame)"/>
  <polygon class="label-frame-white" points="270,14 527,138 527,662 270,786 13,662 13,138" fill="var(--ink-white)"/>
  <polygon class="label-field" points="270,24 517,144 517,656 270,776 23,656 23,144" fill="url(#label-field)"/>
  <polygon class="label-inner-line" points="270,40 502,153 502,647 270,760 38,647 38,153" fill="none" stroke="url(#gold-frame)" stroke-width="3"/>

  <!-- wheat ornaments -->
  <rect class="wheat-ornament" x="182" y="90" width="46" height="46" rx="20" fill="var(--gold)" role="img" aria-label="Golden wheat ear ornament"/>
  <rect class="wheat-ornament" x="312" y="90" width="46" height="46" rx="20" fill="var(--gold)" role="img" aria-label="Golden wheat ear ornament"/>

  <!-- style name -->
  <path class="script-underline" d="M165 285 Q270 300 375 285" fill="none" stroke="var(--gold)" stroke-width="3"/>
  <text class="label-script" x="270" y="262" text-anchor="middle" font-size="104">Pilsner</text>

  <!-- ribbon -->
  <g class="brand-ribbon" transform="rotate(-4 270 405)">
    <polygon class="ribbon-tail" points="-60,375 20,375 20,455 -60,455 -35,415" fill="var(--ribbon-red-dark)"/>
    <polygon class="ribbon-tail" points="520,355 600,355 575,395 600,435 520,435" fill="var(--ribbon-red-dark)"/>
    <rect class="ribbon-face" x="-20" y="345" width="580" height="110" fill="url(#ribbon-face)"/>
    <rect class="ribbon-edge" x="-20" y="355" width="580" height="90" fill="none" stroke="var(--ink-white)" stroke-width="4"/>
    <text class="brand-name" x="270" y="432" text-anchor="middle" font-size="76" stroke="var(--ink-dark)" stroke-width="3" paint-order="stroke">TIDEWELL</text>
  </g>

  <!-- tagline and specs -->
  <text class="label-tagline" x="270" y="620" text-anchor="middle" font-size="54">Craft Beer Brand</text>
  <text class="label-specs" x="200" y="690" text-anchor="middle" font-size="30">19,5%</text>
  <text class="label-specs" x="340" y="690" text-anchor="middle" font-size="30">75 cl</text>
</svg>
</body>
</html>
```